**** Web design project for VornaSoft ****

For my ICT company VornaSoft I need a website.

We design, build and host web-applications and we have our own CMS product. In the references part we want to show sample websites (thumbnails) + links.

It should look modern (WEB 2.0), rounded corners.

I want the following menu' s:
- Home
- Services
- References
- News
- About VornaSoft
- Contact

Sample websites:
See attachments
http://www.plumvest.com
http://www.gadomirbureauwerk.nl

Reason: Want to take some time for feedback and improvements.

Reason: I'm waiting for a black background, with shadow and ambient light. You'll make a good chance!

Industry/Entity Type

It Company

Requirements
Must have
• - Fixed width (1024px), should fit on an IPad2
- Language selection English/Dutch
- Twitter/Facebook/LinkedIn/RSS icons
- Footer for Terms of use and Copyrights
- Search box
- 3 (or more) boxes for information i.e. news, blog or advertisements
Nice to have
• - Footer Site Map
- Contrasting background outside borders
- wide image (rotator) (with transperant sentence block)
- Shadow

```html
<!DOCTYPE html>
<html lang="en">
<head>
<meta charset="utf-8">
<title>VornaSoft – Design, Build, Host</title>
<link rel="stylesheet" href="https://fonts.googleapis.com/css2?family=Questrial&family=Open+Sans:wght@400;600;700&family=Arimo:wght@400;700&family=Tinos:wght@400;700&display=swap">
<style>
:root{
  --ink:#3a3a3a;
  --muted:#555;
  --brand:#1a6f95;
  --brand-dark:#0d4e70;
  --teal:#1592b3;
  --teal-deep:#0b5a78;
  --yellow:#f4f21c;
  --green:#2f9a1d;
  --green-light:#5fd13c;
  --line:#c9c9c9;
  --footer-top:#0f4f66;
  --footer-bottom:#0b3140;
}
*{margin:0;padding:0;box-sizing:border-box}
html,body{width:862px;height:1200px;overflow:hidden}
body{position:relative;background:#e9e9e9;font-family:"Open Sans",sans-serif;color:var(--ink)}
.abs{position:absolute}

/* header */
.site-header{left:0;top:0;width:862px;height:86px;background:linear-gradient(#fafafa,#eaeaea);border-top:5px solid var(--brand-dark)}
.brand{left:86px;top:22px;display:flex;align-items:center;gap:8px}
.brand-mark{width:38px;height:38px;border-radius:50%;background:var(--teal)}
.brand-name{font-family:"Questrial",sans-serif;font-size:24px;color:#5a6a72}
.search{left:410px;top:10px;width:148px;height:19px;border-radius:10px;background:#fff;border:1px solid #d2d2d2;box-shadow:inset 0 1px 2px rgba(0,0,0,.15)}
.search-btn{left:534px;top:10px;width:25px;height:19px;border-radius:10px;background:linear-gradient(var(--green-light),var(--green))}
.lang{top:13px;width:15px;height:11px;border:1px solid #bbb}
.lang-en{left:589px;background:#2b3c8c}
.lang-nl{left:608px;background:linear-gradient(#c2262e 33%,#fff 33% 66%,#1f4595 66%)}
.account{left:645px;top:0;width:125px;height:27px;background:var(--brand-dark);border-radius:0 0 18px 18px;font-family:"Questrial",sans-serif;font-size:10px;color:#fff;display:flex;align-items:center;justify-content:center;gap:9px}
.account .sep{opacity:.7}
.main-nav{left:382px;top:49px;display:flex;align-items:center;font-family:"Questrial",sans-serif;font-size:12px;color:#3d4e57}
.main-nav a{color:inherit;text-decoration:none;padding:0 12px;border-left:1px solid #8a9aa3;line-height:12px}
.main-nav .home{border-left:0;padding:0 10px 0 0}

/* hero */
.hero{left:0;top:86px;width:862px;height:371px;background:radial-gradient(ellipse at 50% 45%,#29b3d6 0%,var(--teal) 35%,var(--teal-deep) 85%)}
.hero-base{left:0;top:358px;width:862px;height:99px;background:linear-gradient(#dcdcdc,#ededed)}
.slogan{left:56px;top:120px;width:192px;text-align:right;font-family:"Questrial",sans-serif;font-weight:400;font-size:46px;line-height:47px;color:var(--yellow)}
.slogan-rule{left:259px;top:126px;width:1px;height:138px;background:rgba(255,255,255,.45)}
.hero-copy{left:270px;top:138px;width:186px;font-family:"Questrial",sans-serif;font-size:10.5px;line-height:13px;color:#fff}
.hero-copy em{font-style:normal;color:#a8f0ff}
.cta{left:229px;top:287px;width:154px;height:26px;border-radius:14px;background:linear-gradient(var(--green-light),var(--green));border:1px solid #1f7011;font-family:"Arimo",sans-serif;font-weight:700;font-size:13px;color:#fff;display:flex;align-items:center;justify-content:center;gap:10px}
.slide-arrow{top:175px}
.shot{left:474px;top:86px;width:274px;height:240px;background:linear-gradient(160deg,#f4f4f4 0%,#e3e3e3 30%,#c8262b 31%,#c8262b 60%,#f1f1f1 61%);box-shadow:4px 6px 16px rgba(0,0,0,.35);transform:skewY(-4deg)}

/* feature boxes */
.features{left:86px;top:334px;width:689px;height:161px;background:linear-gradient(#fbfbfb,#e4e4e4);display:flex;border-bottom:5px solid var(--brand)}
.feature{flex:1;position:relative;border-left:1px solid #d8d8d8;padding:30px 16px 0 17px}
.feature:first-child{border-left:0}
.feature h2{display:flex;align-items:center;gap:10px;font-family:"Questrial",sans-serif;font-weight:400;font-size:20px;color:#333}
.feature h2 i{display:block;width:25px;height:24px;border-radius:50%;background:#8c8c8c}
.feature p{margin-top:8px;font-family:"Arimo",sans-serif;font-size:9.4px;line-height:10.4px;color:#444}
.btn-pill{display:flex;align-items:center;justify-content:center;height:17px;border-radius:9px;background:linear-gradient(#2d8bc0,var(--brand-dark));border:1px solid #083650;font-family:"Arimo",sans-serif;font-weight:700;font-size:8.5px;color:#fff}
.feature .btn-pill{position:absolute;left:40px;top:126px;width:86px}

/* content */
.content{left:86px;top:500px;width:689px;height:355px;background:#fff}
.sidebar{left:560px;top:500px;width:215px;height:355px;background:linear-gradient(90deg,#ededed,#f8f8f8)}
.section-title{font-family:"Questrial",sans-serif;font-weight:400;font-size:14px;color:#333}
.section-title b{font-weight:400;color:var(--brand);font-size:26px;margin-left:6px}
.rule{height:1px;background:var(--line)}
.body-copy{font-family:"Open Sans",sans-serif;font-size:8.3px;line-height:10.4px;color:#444}
.thumb{top:720px;width:116px;height:69px;border:2px solid #e3e3e3;border-radius:5px;background:linear-gradient(160deg,#c8262b 0 30%,#dce4ec 30%,#aab6c2 100%);box-shadow:0 1px 3px rgba(0,0,0,.3)}
.thumb-cap{top:803px;width:125px;font-family:"Arimo",sans-serif;font-size:8.3px;line-height:10px;color:#444}
.thumb-cap a{display:block;margin-top:5px;color:var(--brand);font-size:7.5px;text-decoration:underline}
.news-head{left:569px;top:522px;display:flex;align-items:center;gap:6px;font-family:"Open Sans",sans-serif;font-weight:400;font-size:13.5px;color:var(--teal)}
.news-head i{display:block;width:22px;height:20px;background:#d8d8d8;border:1px solid #aaa;transform:rotate(-8deg)}
.news-item{left:575px;width:180px;font-family:"Open Sans",sans-serif}
.news-item h3{font-size:8.5px;font-weight:700;color:#333}
.news-item p{margin-top:5px;font-size:8.5px;line-height:10.3px;color:#555}
.news-item .date{display:inline-block;margin-top:5px;width:102px;height:14px;line-height:14px;padding-left:5px;background:var(--green);color:#fff;font-size:7px}
.news-item .date em{font-weight:700}

/* newsletter & clients */
.newsletter{left:86px;top:866px;width:390px;height:64px;background:linear-gradient(#f3f3f3,#dcdcdc);border:1px solid #cfcfcf;border-radius:4px 0 0 4px}
.clients{left:476px;top:866px;width:299px;height:64px;background:#fff;border:1px solid #cfcfcf;border-left:0;border-radius:0 4px 4px 0;display:flex;align-items:center;justify-content:space-around;font-family:"Open Sans",sans-serif;font-size:9px;font-weight:700;color:#333}
.subscribe-lead{left:98px;top:881px;font-family:"Tinos",serif;font-size:10px;color:#444}
.subscribe-title{left:98px;top:894px;font-family:"Tinos",serif;font-weight:700;font-size:13px;color:var(--brand)}
.pen{left:214px;top:866px;width:24px;height:24px;background:linear-gradient(135deg,#1e6bb0,#9cc6e8)}
.email{left:241px;top:890px;width:140px;height:19px;background:#fff;border:1px solid #bbb;box-shadow:inset 0 1px 2px rgba(0,0,0,.15);font-family:"Tinos",serif;font-style:italic;font-size:8.5px;color:#777;padding:4px 7px}
.email-btn{left:385px;top:891px;width:64px;height:17px;background:var(--brand-dark);font-family:"Tinos",serif;font-weight:700;font-size:8px;color:#fff;display:flex;align-items:center;justify-content:center}

/* sitemap */
.sitemap{left:86px;top:943px;width:689px;height:150px;background:#e4e4e4;border:1px solid #d3d3d3;border-bottom:0;border-radius:5px 5px 0 0}
.sitemap-col{top:968px;width:104px;font-family:"Open Sans",sans-serif}
.sitemap-col h4{font-size:8.5px;font-weight:400;color:var(--brand);padding-bottom:5px;border-bottom:1px solid #b9b9b9}
.sitemap-col ul{list-style:none;margin-top:6px}
.sitemap-col li{font-size:8px;line-height:13px;color:#444}
.sitemap-col li::before{content:"\25B8";color:var(--teal);margin-right:4px;font-size:7px}

/* footer */
.footer{left:0;top:1090px;width:862px;height:110px;background:var(--footer-top);border-top:5px solid var(--brand)}
.footer-bottom{left:0;top:1150px;width:862px;height:50px;background:linear-gradient(var(--footer-bottom),#0d3a4b)}
.footer-note{left:107px;top:1110px;width:650px;font-family:"Open Sans",sans-serif;font-size:7.7px;line-height:10px;color:#fff}
.footer-brand{left:105px;top:1158px;display:flex;align-items:center;gap:6px;font-family:"Questrial",sans-serif;font-size:16px;color:#9aa8ae}
.footer-brand i{display:block;width:28px;height:28px;border-radius:50%;background:#5f7078}
.legal{left:238px;top:1161px;font-family:"Open Sans",sans-serif;font-size:7.7px;color:#9fb1b8;line-height:16px}
.legal a{color:var(--teal);text-decoration:none}
.follow{left:608px;top:1166px;font-family:"Open Sans",sans-serif;font-size:10px;color:#9fb1b8}
.social{top:1163px;width:19px;height:19px;border-radius:50%;background:linear-gradient(#f2f2f2,#9a9a9a)}
</style>
</head>
<body>

<header class="abs site-header"></header>
<div class="abs brand"><span class="brand-mark"></span><span class="brand-name">VornaSoft</span></div>
<div class="abs search"></div>
<div class="abs search-btn"></div>
<span class="abs lang lang-en" title="English"></span>
<span class="abs lang lang-nl" title="Nederlands"></span>
<div class="abs account"><span>Login</span><span class="sep">|</span><span>Register</span></div>
<nav class="abs main-nav">
  <a class="home" href="#"><svg width="16" height="14" viewBox="0 0 16 14"><path d="M8 1 1 7h2v6h4V9h2v4h4V7h2z" fill="#6d7a80"/></svg></a>
  <a href="#">Services</a><a href="#">References</a><a href="#">News</a><a href="#">About VornaSoft</a><a href="#">Contact</a>
</nav>

<section class="abs hero"></section>
<div class="abs hero-base"></div>
<h1 class="abs slogan">Design<br>Build<br>Host</h1>
<div class="abs slogan-rule"></div>
<p class="abs hero-copy"><em>We design, build and host web applications</em> Maecenas id ornare nisl. Nunc luctus ultrices eros, faucibus venenatis nisi pellentesque ac. Integer convallis, quam nec vulputate pretium, magna justo pretium velit, a luctus leo dui sed est. Quisque mattis eleifend est et placerat mauris..</p>
<div class="abs cta">Get Started <svg width="10" height="12" viewBox="0 0 10 12"><path d="M0 0 10 6 0 12z" fill="#fff"/></svg></div>
<svg class="abs slide-arrow" style="left:26px" width="38" height="68" viewBox="0 0 38 68"><path d="M37 1 2 34l35 33" fill="none" stroke="#bfe6f2" stroke-width="1.5"/></svg>
<svg class="abs slide-arrow" style="left:798px" width="38" height="68" viewBox="0 0 38 68"><path d="M1 1l35 33L1 67" fill="none" stroke="#bfe6f2" stroke-width="1.5"/></svg>
<div class="abs shot" role="img" aria-label="Screenshot of a sample client website in a tilted browser mock-up"></div>

<section class="abs features">
  <div class="feature"><h2><i></i>About</h2><p>Vestibulum vel mi et arcu volutpat aliquam. Suspendisse potenti. Curabitur et lorem convallis leo varius dapibus.</p><a class="btn-pill">Read More</a></div>
  <div class="feature"><h2><i style="border-radius:2px"></i>Activities</h2><p>Vestibulum vel mi et arcu volutpat aliquam. Suspendisse potenti. Curabitur et lorem convallis leo varius dapibus.</p><a class="btn-pill">Read More</a></div>
  <div class="feature"><h2><svg width="25" height="24" viewBox="0 0 25 24"><circle cx="12.5" cy="12" r="8" fill="none" stroke="#7d7d7d" stroke-width="5" stroke-dasharray="3 2.3"/><circle cx="12.5" cy="12" r="5" fill="#8c8c8c"/><circle cx="12.5" cy="12" r="2.2" fill="#eee"/></svg>Services</h2><p>Vestibulum vel mi et arcu volutpat aliquam. Suspendisse potenti. Curabitur et lorem convallis leo varius dapibus.</p><a class="btn-pill">Read More</a></div>
  <div class="feature"><h2><svg width="25" height="24" viewBox="0 0 25 24"><path d="M3 21 17 5a4 4 0 0 1 5 5L9 22" fill="none" stroke="#8c8c8c" stroke-width="2.5"/></svg>Links</h2><p>Vestibulum vel mi et arcu volutpat aliquam. Suspendisse potenti. Curabitur et lorem convallis leo varius dapibus.</p><a class="btn-pill">Read More</a></div>
</section>

<main class="abs content"></main>
<aside class="abs sidebar"></aside>

<h2 class="abs section-title" style="left:106px;top:518px">Who we<b>ARE</b></h2>
<div class="abs rule" style="left:106px;top:548px;width:412px"></div>
<p class="abs body-copy" style="left:106px;top:555px;width:420px">Curabitur eu porttitor neque. Praesent pretium, magna non congue sodales, velit nisi pretium dui, nec aliquam lorem odio eget sapien. Nam posuere metus in libero feugiat luctus. Nullam suscipit lectus sed urna viverra dictum. Maecenas eget elit sed nibh venenatis blandit. Nullam luctus porttitor congue. Duis ultrices, tellus ac vestibulum tristique, eros augue tempor elit, eu tincidunt diam lacus rhoncus tellus. Sed placerat leo quam, at pretium dui. Lorem ipsum dolor sit amet, consectetur adipiscing elit. Pellentesque gravida luctus tortor. Cras nibh erat, euismod ac interdum non, lacinia eu massa. Fusce quis lacus diam, sit amet sollicitudin ante.</p>
<p class="abs body-copy" style="left:106px;top:638px;width:420px">Etiam ac nulla est, eu faucibus dui. Praesent tempus sagittis elementum. Praesent id quam erat, sit amet condimentum neque. Phasellus quis est nisi.</p>

<h2 class="abs section-title" style="left:107px;top:668px">The<b>PORTFOLIO</b></h2>
<div class="abs rule" style="left:106px;top:702px;width:412px"></div>
<svg class="abs" style="left:108px;top:735px" width="20" height="36" viewBox="0 0 20 36"><path d="M19 1 2 18l17 17" fill="none" stroke="#333" stroke-width="1.3"/></svg>
<svg class="abs" style="left:520px;top:735px" width="20" height="36" viewBox="0 0 20 36"><path d="M1 1l17 17L1 35" fill="none" stroke="#333" stroke-width="1.3"/></svg>
<div class="abs thumb" style="left:140px" role="img" aria-label="Thumbnail of a sample client website"></div>
<div class="abs thumb" style="left:264px" role="img" aria-label="Thumbnail of a sample client website"></div>
<div class="abs thumb" style="left:389px" role="img" aria-label="Thumbnail of a sample client website"></div>
<p class="abs thumb-cap" style="left:142px">Integer in elit eu urna fetum placerat maece id ornare nisl.<a href="#">Visit Site</a></p>
<p class="abs thumb-cap" style="left:266px">Integer in elit eu urna fetum placerat maece id ornare nisl.<a href="#">Visit Site</a></p>
<p class="abs thumb-cap" style="left:391px">Integer in elit eu urna fetum placerat maece id ornare nisl.<a href="#">Visit Site</a></p>

<h2 class="abs news-head"><i></i>Recent News and Articles</h2>
<article class="abs news-item" style="top:569px"><h3>LOREM IPSUM DOLOR</h3><p>Integer in elit eu urna fermentum placat maecenas id ornare nisl.</p><span class="date"><em>Posted on</em> 14 MAY 2012</span></article>
<div class="abs rule" style="left:575px;top:637px;width:180px;background:#bbb"></div>
<article class="abs news-item" style="top:650px"><h3>LOREM IPSUM DOLOR</h3><p>Integer in elit eu urna fermentum placat maecenas id ornare nisl.</p><span class="date"><em>Posted on</em> 14 MAY 2012</span></article>
<div class="abs rule" style="left:575px;top:716px;width:180px;background:#bbb"></div>
<article class="abs news-item" style="top:732px"><h3>LOREM IPSUM DOLOR</h3><p>Integer in elit eu urna fermentum placat maecenas id ornare nisl.</p><span class="date"><em>Posted on</em> 14 MAY 2012</span></article>
<div class="abs rule" style="left:575px;top:800px;width:180px;background:#bbb"></div>
<a class="abs btn-pill" style="left:624px;top:812px;width:86px">See All</a>

<section class="abs newsletter"></section>
<p class="abs subscribe-lead">Subscribe to our</p>
<p class="abs subscribe-title">FREE NEWSLETTER</p>
<div class="abs pen" role="img" aria-label="Fountain pen illustration"></div>
<div class="abs email">Type your email here...</div>
<div class="abs email-btn">SUBSCRIBE</div>
<div class="abs clients"><span>Teloria</span><span>Kestrix</span><span>Novadyne</span><span>Aerwyn</span></div>

<section class="abs sitemap"></section>
<nav class="abs sitemap-col" style="left:106px"><h4>Footer Links</h4><ul><li>Etiam ac nulla est</li><li>Etiam ac nulla est</li><li>Etiam ac nulla est</li><li>Etiam ac nulla est</li><li>Etiam ac nulla est</li><li>Etiam ac nulla est</li></ul></nav>
<nav class="abs sitemap-col" style="left:238px"><h4>Footer Links</h4><ul><li>Etiam ac nulla est</li><li>Etiam ac nulla est</li><li>Etiam ac nulla est</li><li>Etiam ac nulla est</li><li>Etiam ac nulla est</li><li>Etiam ac nulla est</li></ul></nav>
<nav class="abs sitemap-col" style="left:375px"><h4>Footer Links</h4><ul><li>Etiam ac nulla est</li><li>Etiam ac nulla est</li><li>Etiam ac nulla est</li><li>Etiam ac nulla est</li><li>Etiam ac nulla est</li><li>Etiam ac nulla est</li></ul></nav>
<nav class="abs sitemap-col" style="left:509px"><h4>Footer Links</h4><ul><li>Etiam ac nulla est</li><li>Etiam ac nulla est</li><li>Etiam ac nulla est</li><li>Etiam ac nulla est</li><li>Etiam ac nulla est</li><li>Etiam ac nulla est</li></ul></nav>
<nav class="abs sitemap-col" style="left:644px"><h4>Footer Links</h4><ul><li>Etiam ac nulla est</li><li>Etiam ac nulla est</li><li>Etiam ac nulla est</li><li>Etiam ac nulla est</li><li>Etiam ac nulla est</li><li>Etiam ac nulla est</li></ul></nav>

<footer class="abs footer"></footer>
<div class="abs footer-bottom"></div>
<p class="abs footer-note">Quisque ultricies dolor sit amet enim malesuada consectetur. Maecenas vulputate tellus nec orci posuere interdum. Suspendisse potenti. Fusce quis enim massa. Ut tempor turpis non dolor feugiat vel tempus ligula malesuada. Ut hendrerit hendrerit dui, quis aliquam tortor facilisis eu. Nulla sodales rutrum dolor.</p>
<div class="abs footer-brand"><i></i>VornaSoft</div>
<p class="abs legal">Copyright 2012 VornaSoft . All rights reserved.<br><a href="#">Privacy Policy</a> &nbsp;|&nbsp; <a href="#">Disclaimer</a></p>
<span class="abs follow">Follow:</span>
<span class="abs social" style="left:655px"></span>
<span class="abs social" style="left:681px"></span>
<span class="abs social" style="left:707px"></span>
<span class="abs social" style="left:734px"></span>

</body>
</html>
```